Etiketten für Charity Bier gesucht
Zielgruppe
Wir engagieren uns ehrenamtlich für Kinder in Afrika.
In Einsatz-Teams von freiwilligen Helfern, sammeln wir während 8 Monaten Spendengelder, um Kindern in Townships's Südafrikas eine Zukunft zu bauen, in dem wir nicht staatliche Kindertagesstätten engagierter einheimischer Frauen umbauen.
Vorher bestehen die KITA's nur aus rostigen Wellblechhütten, welche nicht isoliert sind und auf dem KITA Gelände befindet sich weder Rasen, noch ein Spielplatz.
Aufgabenstellung
Um Spenden zu sammeln, möchten wir ein Charity Bier auf den Markt bringen.
Infos zu den Maßen der Etiketten: Sie sollten nicht breiter als 8 cm sein. Wichtig ist, dass sich in der Ecke links oben keine Angaben befinden, da die obere linke Kante schräg nach oben verlaufen wird. Welche Angaben müssen zwingend auf den Etiketten zu finden sein?
Die Promill-Angaben (5.2% VOL)
Inhalts-Angabe (33cl) das Logo des Bierherstellers sollte auch mit auf die Etikette (nicht all zu gross) (siehe Bild Nr.2)
Die Info's zum Bier (Biersorte: Tannfelsbräu ORIGINAL)
Der Name des Bier's sollte Charity Bier sein.
Wir möchten auf der Etikette auch folgendes unbedingt vermerken:
'Diese Flache (Bier) füllt 10 Breischalen für Kinder in Afrika'
Ansonsten haben wir überhaupt keine Vorstellung, was wir wörtlich noch auf die Etikette packen möchten (vielleicht fällt euch ja noch was tolles ein:-)
Was wir uns vom Design her so vorstellen:
Ich habe noch 3 Bilder (siehe Bild 3-4) dazugefügt, mit Designs, welche mir auf Anhieb sehr sehr gut gefallen (damit ihr einen Anhaltspunkt habt:-) Aber ich lasse mich auch gerne von anderen Design-Formen überraschen.

```html
<!DOCTYPE html>
<html lang="de">
<head>
<meta charset="utf-8">
<title>Charity Bier – Etikett</title>
<link href="https://fonts.googleapis.com/css2?family=Alfa+Slab+One&family=Barlow:wght@400;700&family=Barlow+Semi+Condensed:wght@700&display=swap" rel="stylesheet">
<style>
  :root {
    --paper-light: #d3bd97;
    --paper-mid: #c6ad83;
    --paper-dark: #b39a70;
    --ink: #231f1b;
    --ink-soft: #3a322a;
    --rule: #6e5f52;
    --amber: #f6ad2c;
    --white: #ffffff;
    --letter-face: #a89272;
  }
  * { margin: 0; padding: 0; box-sizing: border-box; }
  html, body { width: 960px; height: 1200px; overflow: hidden; background: var(--paper-mid); }
  .label {
    position: relative;
    width: 960px;
    height: 1200px;
    overflow: hidden;
    background: radial-gradient(ellipse at 50% 35%, var(--paper-light) 0%, var(--paper-mid) 60%, var(--paper-dark) 100%);
    font-family: "Barlow", Arial, sans-serif;
    color: var(--ink);
  }
  .brand-row {
    position: absolute;
    top: 128px; left: 0; width: 960px;
    display: flex; align-items: center; justify-content: center; gap: 34px;
  }
  .double-rule {
    width: 166px; height: 10px;
    border-top: 3px solid var(--rule);
    border-bottom: 3px solid var(--rule);
  }
  .brand-name {
    font-family: "Barlow Semi Condensed", Arial, sans-serif;
    font-weight: 700;
    font-size: 40px;
    color: var(--amber);
    line-height: 1;
  }
  .beer-title {
    position: absolute;
    left: 0; width: 960px;
    text-align: center;
    font-family: "Alfa Slab One", Georgia, serif;
    font-weight: 400;
    color: var(--letter-face);
    -webkit-text-stroke: 3px var(--ink);
    line-height: 1;
    white-space: nowrap;
    text-shadow:
      2px 2px 0 var(--ink-soft), 4px 4px 0 var(--ink-soft),
      6px 6px 0 var(--ink-soft), 8px 8px 0 var(--ink-soft);
  }
  .beer-title--charity { top: 212px; font-size: 178px; }
  .beer-title--bier { top: 392px; font-size: 290px; }
  .specs-row {
    position: absolute;
    top: 712px; left: 0; width: 960px;
    display: flex; align-items: center; justify-content: center; gap: 22px;
  }
  .specs-row .double-rule { width: 162px; }
  .specs {
    font-weight: 700;
    font-size: 28px;
    letter-spacing: 1px;
    line-height: 1;
    color: var(--ink);
  }
  .charity-note {
    position: absolute;
    top: 788px; left: 0; width: 960px;
    text-align: center;
    font-size: 22px;
    color: var(--ink);
  }
  .variety-band {
    position: absolute;
    top: 856px; left: 0; width: 960px; height: 80px;
    background: var(--white);
    display: flex; align-items: center;
  }
  .variety-band__fill {
    width: 100%; height: 60px;
    background: var(--amber);
    display: flex; align-items: center; justify-content: center;
    font-family: "Barlow Semi Condensed", Arial, sans-serif;
    font-weight: 700;
    font-size: 38px;
    letter-spacing: 1.5px;
    color: var(--ink);
  }
  .stripe-field {
    position: absolute;
    top: 936px; left: 0; width: 960px; height: 264px;
    background: linear-gradient(100deg, #2c2620 0%, #6f5f48 45%, #2c2620 70%, #8a7658 100%);
  }
</style>
</head>
<body>
<main class="label">
  <div class="brand-row">
    <span class="double-rule"></span>
    <span class="brand-name">Tannfelsbräu</span>
    <span class="double-rule"></span>
  </div>

  <h1 class="beer-title beer-title--charity">Charity</h1>
  <div class="beer-title beer-title--bier">Bier</div>

  <div class="specs-row">
    <span class="double-rule"></span>
    <span class="specs">5.2% VOL // 33 cl</span>
    <span class="double-rule"></span>
  </div>

  <p class="charity-note">Diese Flasche Bier füllt 10 KALU Breischalen für Kinder in Afrika</p>

  <div class="variety-band">
    <div class="variety-band__fill">Tannfelsbräu ORIGINAL</div>
  </div>

  <div class="stripe-field" role="img" aria-label="Zebrastreifen-Muster in Schwarz auf Papierbeige"></div>
</main>
</body>
</html>
```